New Business Card for Casual Beachfront Cafe

Quirky Beachfront Cafe at Moana, South Australia needs a DOUBLE SIDED business card to print on PrintHarbor.

Target Market(s)

Business Cards sit on the counter for Guests to take with them. Please view our website www.saltreefcafe.com.au to get a feel for the Cafe. You may also view our Instagram at @saltreefcafe

Industry/Entity Type

Cafe / Restaurant

Contact Information for Business Card

Information equivalent to: Breakfast, Lunch, Dinner, Coffee, Takeaway / 117 Parade Coralby SA 5290 / Menu & Opening Hours: www.saltreefcafe.com.au / ph (08) 8461 9273

Requirements
Must have
• Information equivalent to: Breakfast, Lunch, Dinner, Coffee, Takeaway / 117 Parade Coralby SA 5290 / Menu & Opening Hours: www.saltreefcafe.com.au / ph (08) 8461 9273
Nice to have
• Potentially some of our trademark colours (Cafe can be searched via Seekly)
Should not have
• Must NOT have image of the building. May have the logo provided on one side but not necessarily, depending on how you wish to design the card

```html
<!DOCTYPE html>
<html lang="en">
<head>
<meta charset="utf-8">
<title>Salt Reef Cafe — Business Card</title>
<link rel="stylesheet" href="https://fonts.googleapis.com/css2?family=Jost:wght@400;500;700;800&display=swap">
<style>
  :root {
    --sun: #f2ea0c;
    --navy: #12477d;
    --page: #f3f3f3;
  }
  * { margin: 0; padding: 0; box-sizing: border-box; }
  html, body { width: 1200px; height: 1200px; overflow: hidden; }
  body {
    position: relative;
    background: var(--page);
    font-family: "Jost", sans-serif;
    color: var(--navy);
  }
  .card {
    position: absolute;
    border-radius: 52px;
    overflow: hidden;
  }

  /* ---------- Front ---------- */
  .card-front {
    left: 179px; top: 101px;
    width: 833px; height: 476px;
    background: var(--navy);
  }
  .front-field { position: absolute; inset: 0; }
  .front-brand {
    position: absolute;
    left: 101px; top: 32px;
    width: 200px; height: 384px;
    display: flex; align-items: center; justify-content: center;
  }
  .front-brand-name {
    transform: rotate(-90deg);
    white-space: nowrap;
    text-align: center;
    font-weight: 800;
    font-size: 64px;
    line-height: 0.95;
    letter-spacing: 1px;
    color: var(--navy);
  }
  .front-heading {
    position: absolute;
    left: 468px; top: 76px;
  }
  .front-title {
    font-weight: 700;
    font-size: 37px;
    line-height: 1;
    letter-spacing: 0.5px;
    white-space: nowrap;
  }
  .front-role {
    font-weight: 500;
    font-size: 19px;
    letter-spacing: 0.5px;
    margin-top: 2px;
  }
  .contact-list {
    position: absolute;
    left: 465px; top: 248px;
    list-style: none;
  }
  .contact-item {
    display: flex; align-items: center;
    height: 35px;
    margin-bottom: 14px;
    color: var(--sun);
    font-weight: 500;
    font-size: 20px;
    letter-spacing: 0.5px;
    white-space: nowrap;
  }
  .contact-item:last-child { margin-top: 19px; }
  .contact-icon {
    flex: none;
    width: 35px; height: 35px;
    border-radius: 50%;
    background: var(--sun);
    display: flex; align-items: center; justify-content: center;
    margin-right: 11px;
  }
  .contact-icon svg { width: 20px; height: 20px; }

  /* ---------- Back ---------- */
  .card-back {
    left: 199px; top: 642px;
    width: 809px; height: 461px;
    background: var(--sun);
  }
  .back-brand {
    position: absolute;
    left: 0; right: 0; top: 112px;
    text-align: center;
    font-weight: 800;
    font-size: 66px;
    line-height: 0.98;
    letter-spacing: 1px;
  }
  .back-web {
    position: absolute;
    left: 0; right: 0; top: 307px;
    display: flex; align-items: center; justify-content: center;
    font-weight: 500;
    font-size: 22px;
    letter-spacing: 0.5px;
  }
  .back-web .contact-icon {
    width: 32px; height: 32px;
    background: var(--navy);
    margin-right: 10px;
  }
  .back-band {
    position: absolute;
    left: 0; right: 0; bottom: 0;
    height: 86px;
    background: var(--navy);
    display: flex; align-items: center; justify-content: center;
    color: var(--sun);
    font-weight: 500;
    font-size: 22.5px;
    letter-spacing: 0.5px;
  }
</style>
</head>
<body>

<section class="card card-front">
  <svg class="front-field" viewBox="0 0 833 476" aria-hidden="true">
    <path fill="var(--sun)" d="M0 0 H833 V192 H478 A50 50 0 0 0 428 242 V401 A50 50 0 0 1 378 451 H0 Z"/>
  </svg>

  <div class="front-brand">
    <p class="front-brand-name">SALT REEF<br>CAFE</p>
  </div>

  <div class="front-heading">
    <h1 class="front-title">SALT REEF CAFE</h1>
    <p class="front-role">FOUNDER/CEO</p>
  </div>

  <ul class="contact-list">
    <li class="contact-item">
      <span class="contact-icon">
        <svg viewBox="0 0 24 24"><path fill="var(--navy)" d="M6.6 2.5l3 3.4-1.8 2.4c1.2 2.9 3.4 5.1 6.3 6.4l2.4-1.8 3.4 3-1.9 3.4C11 19 5 13 3.1 4.4z"/></svg>
      </span>
      ph (08) 8461 9273
    </li>
    <li class="contact-item">
      <span class="contact-icon">
        <svg viewBox="0 0 24 24"><rect x="3" y="6" width="18" height="12" fill="none" stroke="var(--navy)" stroke-width="1.8"/><path d="M3 6l9 7 9-7M3 18l7-6M21 18l-7-6" fill="none" stroke="var(--navy)" stroke-width="1.5"/></svg>
      </span>
      hello@saltreefcafe.com.au
    </li>
    <li class="contact-item">
      <span class="contact-icon">
        <svg viewBox="0 0 24 24"><path fill="none" stroke="var(--navy)" stroke-width="2.2" d="M12 21.5s-6.5-7-6.5-11.5a6.5 6.5 0 0 1 13 0c0 4.5-6.5 11.5-6.5 11.5z"/><circle cx="12" cy="10" r="2.3" fill="var(--navy)"/></svg>
      </span>
      117 Parade Coralby SA 5290
    </li>
    <li class="contact-item">
      <span class="contact-icon">
        <svg viewBox="0 0 24 24" fill="none" stroke="var(--navy)" stroke-width="1.5"><circle cx="12" cy="12" r="9"/><ellipse cx="12" cy="12" rx="4" ry="9"/><path d="M3 12h18M4.5 7.5h15M4.5 16.5h15M12 3v18"/></svg>
      </span>
      www.saltreefcafe.com.au
    </li>
  </ul>
</section>

<section class="card card-back">
  <p class="back-brand">SALT REEF<br>CAFE</p>
  <p class="back-web">
    <span class="contact-icon">
      <svg viewBox="0 0 24 24" fill="none" stroke="var(--sun)" stroke-width="1.5"><circle cx="12" cy="12" r="9"/><ellipse cx="12" cy="12" rx="4" ry="9"/><path d="M3 12h18M4.5 7.5h15M4.5 16.5h15M12 3v18"/></svg>
    </span>
    www.saltreefcafe.com.au
  </p>
  <p class="back-band">Breakfast, Lunch, Dinner, Coffee, Takeaway</p>
</section>

</body>
</html>
```